Tervane Electronic Security Web Site

We need a web site for our new company based in Sydney Australia.
We specialize in consulting supplying and installing electronic security systems. These include CCTV, Access control, Alarms, Intercom and Network cabling.
We pride our selves in giving our customers peace of mind giving back security and freedom to our customers. We pride in customer service quality products and expertise with and we do the job as though it is for our personal friends and family.
We need to be able to edit web site contents and update information.

```html
<!DOCTYPE html>
<html lang="en">
<head>
<meta charset="utf-8">
<title>Tervane Electronic Security</title>
<link href="https://fonts.googleapis.com/css2?family=Open+Sans:wght@400;600;700&display=swap" rel="stylesheet">
<style>
:root{
  --green:#3d9c49;
  --green-bright:#12c11f;
  --green-text:#3f9e4c;
  --ink:#1e1e1e;
  --white:#ffffff;
  --orange-top:#ffa233;
  --orange-bottom:#f07a00;
  --hero-dark:#1c3a44;
  --hero-mid:#5f8f98;
  --hero-light:#d6e6e8;
  --rule:#d9d9d9;
}
*{margin:0;padding:0;box-sizing:border-box}
html,body{width:1200px;height:943px;overflow:hidden;background:var(--white);font-family:"Open Sans",Arial,sans-serif}
.page{position:relative;width:1200px;height:943px}
.hero{position:absolute;left:0;top:0;width:1200px;height:665px;
  background:
    radial-gradient(ellipse 420px 300px at 600px 260px, var(--hero-light) 0%, rgba(214,230,232,0) 100%),
    radial-gradient(ellipse 300px 260px at 600px 560px, #20242a 0%, rgba(32,36,42,0) 100%),
    linear-gradient(180deg, var(--hero-dark) 0%, var(--hero-mid) 45%, #3c4a52 100%);}
.brand{position:absolute;left:128px;top:17px;font-size:35px;font-weight:600;color:var(--white);letter-spacing:.2px}
.callout{position:absolute;left:906px;top:18px;display:flex;align-items:center;gap:6px}
.callout-label{display:block;font-size:18px;color:var(--green-text);line-height:18px;font-weight:600}
.callout-number{display:block;font-size:24px;color:var(--white);font-weight:600;line-height:26px}
.nav{position:absolute;left:128px;top:81px;width:943px;height:48px;border-top:1px solid rgba(255,255,255,.35);border-bottom:1px solid rgba(255,255,255,.35);display:flex}
.nav a{display:block;height:46px;line-height:48px;padding:0 20px;color:var(--white);text-decoration:none;font-size:15px;border-right:1px solid rgba(255,255,255,.25)}
.nav a.active{background:var(--green);padding:0 18px}
.nav a:nth-child(2){padding:0 20px 0 32px}
.nav a:last-of-type{border-right:none}
.social{position:absolute;right:0;top:15px;display:flex;gap:9px}
.social span{width:13px;height:13px;border-radius:2px;display:block}
.s1{background:#f07a00}.s2{background:#c3281e}.s3{background:#3b5998}.s4{background:#3fb6e6}
.arrow{position:absolute;top:315px}
.arrow-left{left:44px}.arrow-right{left:1097px}
.headline{position:absolute;left:0;top:338px;width:1200px;text-align:center;text-transform:uppercase;font-size:41px;line-height:42px}
.headline strong{display:block;color:var(--ink);font-weight:700}
.headline span{display:block;color:var(--green-text);font-weight:400}
.cta{position:absolute;left:508px;top:437px;width:187px;height:48px;border-radius:5px;border:1px solid #e06f00;background:linear-gradient(180deg,var(--orange-top) 0%,#ff9416 50%,var(--orange-bottom) 51%,var(--orange-bottom) 100%);color:var(--white);font-weight:700;font-size:19px;text-align:center;line-height:46px;text-transform:uppercase;text-decoration:none}
.services{position:absolute;left:0;top:552px;width:1200px;height:230px}
.service{position:absolute;top:0;width:200px;height:230px}
.service svg{position:absolute;left:0;top:0}
.service-label{position:absolute;left:0;width:200px;text-align:center;color:var(--white);font-weight:700;font-size:17px;line-height:21px;text-transform:uppercase}
.footer{position:absolute;left:128px;top:846px;width:943px;border-top:1px solid var(--rule);text-align:center}
.footer-nav{margin-top:20px;font-size:11px;color:#111}
.footer-nav a{color:#111;text-decoration:none}
.footer-nav i{font-style:normal;margin:0 16px}
.copyright{font-size:12px;color:var(--green-text);margin-top:3px}
.footer .social{position:static;justify-content:center;margin-top:6px}
</style>
</head>
<body>
<div class="page">
  <div class="hero" role="img" aria-label="Photo of business people in suits holding black umbrellas and orange folders in the rain"></div>

  <div class="brand">Tervane Electronic</div>
  <div class="callout">
    <svg width="24" height="38" viewBox="0 0 24 38"><rect x="2" y="1" width="20" height="36" rx="3" fill="none" stroke="#fff" stroke-width="2.5"/><line x1="4" y1="7" x2="20" y2="7" stroke="#fff" stroke-width="2"/><line x1="4" y1="29" x2="20" y2="29" stroke="#fff" stroke-width="2"/><circle cx="12" cy="33" r="1.8" fill="#fff"/></svg>
    <div><span class="callout-label">Call Now!</span><span class="callout-number">987 6543 210</span></div>
  </div>

  <nav class="nav">
    <a class="active" href="#">ABOUT</a>
    <a href="#">SERVICES</a>
    <a href="#">PRODUCTS</a>
    <a href="#">NEWS</a>
    <a href="#">CONTACTS</a>
    <div class="social"><span class="s1"></span><span class="s2"></span><span class="s3"></span><span class="s4"></span></div>
  </nav>

  <svg class="arrow arrow-left" width="50" height="94" viewBox="0 0 50 94"><polyline points="48,2 3,47 48,92" fill="none" stroke="#fff" stroke-width="2.5"/></svg>
  <svg class="arrow arrow-right" width="50" height="94" viewBox="0 0 50 94"><polyline points="2,2 47,47 2,92" fill="none" stroke="#fff" stroke-width="2.5"/></svg>

  <h1 class="headline"><strong>Security services and</strong><span>management at fair prices.</span></h1>
  <a class="cta" href="#">Learn more</a>

  <section class="services">
    <div class="service" style="left:140px">
      <svg width="200" height="230" viewBox="0 0 200 230"><polygon points="100,3 197,59 197,171 100,227 3,171 3,59" fill="var(--green-bright)" stroke="#fff" stroke-width="4"/>
        <g fill="#fff"><polygon points="55,78 120,66 128,92 62,104"/><rect x="52" y="98" width="14" height="12"/><rect x="104" y="98" width="8" height="22"/><rect x="104" y="116" width="36" height="8"/><rect x="138" y="108" width="8" height="26"/></g></svg>
      <div class="service-label" style="top:150px">CCTV</div>
    </div>
    <div class="service" style="left:368px">
      <svg width="200" height="230" viewBox="0 0 200 230"><polygon points="100,3 197,59 197,171 100,227 3,171 3,59" fill="var(--green)" stroke="#fff" stroke-width="4"/>
        <rect x="54" y="55" width="92" height="72" rx="8" fill="none" stroke="#fff" stroke-width="6"/><rect x="88" y="64" width="22" height="28" fill="#fff"/><rect x="84" y="90" width="30" height="32" rx="6" fill="#fff"/></svg>
      <div class="service-label" style="top:138px">Access<br>Control</div>
    </div>
    <div class="service" style="left:597px">
      <svg width="200" height="230" viewBox="0 0 200 230"><polygon points="100,3 197,59 197,171 100,227 3,171 3,59" fill="var(--green)" stroke="#fff" stroke-width="4"/>
        <g fill="#fff"><path d="M82,120 V86 a18,18 0 0 1 36,0 V120 Z"/><rect x="74" y="118" width="52" height="12" rx="3"/><rect x="97" y="42" width="6" height="18"/><rect x="68" y="52" width="6" height="16" transform="rotate(-40 71 60)"/><rect x="126" y="52" width="6" height="16" transform="rotate(40 129 60)"/><rect x="50" y="72" width="18" height="5"/><rect x="132" y="72" width="18" height="5"/></g></svg>
      <div class="service-label" style="top:142px">Alarms</div>
    </div>
    <div class="service" style="left:827px">
      <svg width="200" height="230" viewBox="0 0 200 230"><polygon points="100,3 197,59 197,171 100,227 3,171 3,59" fill="var(--green)" stroke="#fff" stroke-width="4"/>
        <path d="M118,60 C90,58 80,78 98,92 C118,106 110,122 74,126" fill="none" stroke="#fff" stroke-width="5" stroke-linecap="round"/><rect x="116" y="50" width="16" height="16" fill="#fff"/></svg>
      <div class="service-label" style="top:142px">Network<br>Cabling</div>
    </div>
  </section>

  <footer class="footer">
    <div class="footer-nav"><a href="#">HOME</a><i>|</i><a href="#">ABOUT US</a><i>|</i><a href="#">SERVICES</a><i>|</i><a href="#">OUR CONTACTS</a><i>|</i><a href="#">BLOG</a></div>
    <div class="copyright">© 2014 Tervane-Electronic</div>
    <div class="social"><span class="s1"></span><span class="s2"></span><span class="s3"></span><span class="s4"></span></div>
  </footer>
</div>
</body>
</html>
```